Luxury Photoalbum manufacturer needs banner design 8'x8'

We need a banner design for trade show purposes. We supply luxury one-of-a-kind photo albums to boudoir photographers. Our customers are female professional photographers - mostly in the age range of 26 - 40.Design needs to appeal to business women in this age range who see their business help empower women.Follow our website for our current look and feel. www.velvetkeepsake.com
It needs to be 8'x8'

Target Market(s)

Women professional boudoir photographers

Industry/Entity Type

Professional Photography

Font styles to use
Serif

Requirements
Must have
• Feminine but professional look and feel
• Need the LOGO to be very dominant
• Needs to be reasonably consistent with our website - www.velvetkeepsake.com
Nice to have
• Not necessary to use all the images - can use as few or many as makes sense.

```html
<!DOCTYPE html>
<html lang="en">
<head>
<meta charset="utf-8">
<title>Velvet Keepsake – Trade Show Banner</title>
<link rel="stylesheet" href="https://fonts.googleapis.com/css2?family=Open+Sans:wght@400;600;700&family=Tinos:wght@700&display=swap">
<style>
  :root {
    --paper: #efeced;
    --brand-red: #ec1f24;
    --navy: #12132e;
    --ink: #111111;
  }
  html, body {
    margin: 0;
    padding: 0;
    width: 1200px;
    height: 1200px;
    overflow: hidden;
    background: var(--paper);
  }
  .banner {
    position: relative;
    width: 1200px;
    height: 1200px;
    background: var(--paper);
    overflow: hidden;
    font-family: "Open Sans", Arial, sans-serif;
  }
  .banner__graphics {
    position: absolute;
    inset: 0;
  }
  .brand-name {
    position: absolute;
    left: 40px;
    top: 150px;
    width: 390px;
    text-align: center;
    color: var(--brand-red);
    font-weight: 600;
    line-height: 1.05;
    margin: 0;
  }
  .brand-name__line {
    display: block;
    letter-spacing: 0.12em;
  }
  .brand-name__line--top { font-size: 74px; }
  .brand-name__line--bottom { font-size: 56px; margin-top: 8px; }
  .tagline {
    position: absolute;
    left: 78px;
    top: 990px;
    margin: 0;
    color: var(--brand-red);
    line-height: 1;
  }
  .tagline__small {
    display: block;
    font-size: 37px;
    font-weight: 400;
  }
  .tagline__big {
    display: block;
    font-size: 58px;
    font-weight: 700;
    margin: 4px 0 6px;
    letter-spacing: -0.01em;
  }
  .web-address {
    position: absolute;
    right: 49px;
    top: 1130px;
    margin: 0;
    font-family: "Tinos", "Times New Roman", serif;
    font-weight: 700;
    font-size: 28px;
    color: var(--ink);
  }
</style>
</head>
<body>
<main class="banner">
  <svg class="banner__graphics" width="1200" height="1200" viewBox="0 0 1200 1200">
    <defs>
      <linearGradient id="tone-velvet-stack" x1="0" y1="0" x2="1" y2="1">
        <stop offset="0" stop-color="#8a1a2a"/>
        <stop offset="0.5" stop-color="#7a6a5e"/>
        <stop offset="1" stop-color="#9b1f2e"/>
      </linearGradient>
      <linearGradient id="tone-cover-portrait" x1="0" y1="0" x2="0" y2="1">
        <stop offset="0" stop-color="#8c6a55"/>
        <stop offset="0.6" stop-color="#6b2a2a"/>
        <stop offset="1" stop-color="#9a9690"/>
      </linearGradient>
      <linearGradient id="tone-silver-box" x1="0" y1="0" x2="1" y2="1">
        <stop offset="0" stop-color="#b9bcbb"/>
        <stop offset="0.5" stop-color="#6f6f70"/>
        <stop offset="1" stop-color="#2b2b2d"/>
      </linearGradient>
      <linearGradient id="tone-textured-stack" x1="0" y1="0" x2="0" y2="1">
        <stop offset="0" stop-color="#c4b48e"/>
        <stop offset="0.35" stop-color="#b8202c"/>
        <stop offset="0.7" stop-color="#1d1d4d"/>
        <stop offset="1" stop-color="#151518"/>
      </linearGradient>
    </defs>

    <polygon class="accent accent--red-top" fill="var(--brand-red)" points="685,0 1070,0 1070,85 878,192 685,85"/>
    <polygon class="accent accent--navy" fill="var(--navy)" points="1098,0 1200,0 1200,142 1098,85"/>
    <polygon class="accent accent--red-side" fill="var(--brand-red)" points="1089,603 1200,549 1200,909 1089,846"/>

    <g role="img" aria-label="Photo: stack of red and taupe velvet albums with a pearl necklace">
      <polygon fill="url(#tone-velvet-stack)" points="669,108 862,223 862,455 669,570 477,455 477,223"/>
    </g>
    <g role="img" aria-label="Photo: album with a portrait cover and red snakeskin spine">
      <polygon fill="url(#tone-cover-portrait)" points="1088,110 1281,225 1281,455 1088,570 895,455 895,225"/>
    </g>
    <g role="img" aria-label="Photo: silver album boxes tied with satin ribbons">
      <polygon fill="url(#tone-silver-box)" points="471,484 664,599 664,830 471,945 278,830 278,599"/>
    </g>
    <g role="img" aria-label="Photo: stack of gold, red, navy and black textured albums">
      <polygon fill="url(#tone-textured-stack)" points="877,484 1070,599 1070,830 877,945 684,830 684,599"/>
    </g>
  </svg>

  <h1 class="brand-name">
    <span class="brand-name__line brand-name__line--top">VELVET</span>
    <span class="brand-name__line brand-name__line--bottom">KEEPSAKE</span>
  </h1>

  <p class="tagline">
    <span class="tagline__small">THE</span>
    <span class="tagline__big">LUXURIOUS</span>
    <span class="tagline__small">ALBUMS</span>
  </p>

  <p class="web-address">www.velvetkeepsake.com</p>
</main>
</body>
</html>
```